Brightpath STEM Academy by graduating students from college in two years

Based on the logo design, create stationary and business cards for
Dr. Velimir T Osunde, CEO, (703) 482-1630
and Mirela Thorpe, Respresentative, (301) 557-2048
Address: 4417 Marbleton Lane, Faurfax Station, VA 22061
Incorporate elelments of the logo

Target Market(s)

USA

Other font styles liked:
• match with the logo type style

```html
<!DOCTYPE html>
<html lang="en">
<head>
<meta charset="utf-8">
<title>Letterhead – Dr. Velimir T. Osunde</title>
<link rel="stylesheet" href="https://fonts.googleapis.com/css2?family=Crimson+Pro:wght@400;500&display=swap">
<style>
  :root {
    --navy: #11385b;
    --gold: #f6bf1f;
    --paper: #ffffff;
    --ghost: #eef0f2;
  }
  * { margin: 0; padding: 0; box-sizing: border-box; }
  html, body {
    width: 800px;
    height: 1200px;
    overflow: hidden;
    background: var(--paper);
  }
  .letterhead {
    position: relative;
    width: 800px;
    height: 1200px;
    background: var(--paper);
    font-family: "Crimson Pro", Georgia, serif;
    color: var(--navy);
  }
  .header-rule {
    position: absolute;
    top: 192px;
    height: 4px;
    background: var(--navy);
  }
  .header-rule--left { left: 55px; width: 200px; }
  .header-rule--right { right: 55px; width: 200px; }
  .brand {
    position: absolute;
    top: 194px;
    left: 400px;
    transform: translate(-50%, -50%);
    display: flex;
    align-items: center;
    gap: 10px;
    white-space: nowrap;
  }
  .brand__dot {
    width: 14px;
    height: 14px;
    border-radius: 50%;
    background: var(--gold);
  }
  .brand__name {
    font-size: 22px;
    font-weight: 500;
    color: var(--navy);
    letter-spacing: 0.02em;
  }
  .watermark {
    position: absolute;
    top: 625px;
    left: 400px;
    transform: translate(-50%, -50%);
    font-size: 40px;
    font-weight: 500;
    color: var(--ghost);
    white-space: nowrap;
  }
  .footer-rule {
    position: absolute;
    top: 1049px;
    left: 55px;
    width: 690px;
    height: 3px;
    background: var(--gold);
  }
  .contact {
    position: absolute;
    top: 1070px;
    left: 0;
    width: 800px;
    text-align: center;
  }
  .contact__name {
    font-size: 30px;
    font-weight: 400;
    line-height: 36px;
  }
  .contact__address,
  .contact__phone {
    font-size: 18px;
    line-height: 29px;
  }
</style>
</head>
<body>
  <div class="letterhead">
    <div class="header-rule header-rule--left"></div>
    <div class="header-rule header-rule--right"></div>
    <div class="brand">
      <span class="brand__dot"></span>
      <span class="brand__name">Brightpath STEM Academy</span>
    </div>

    <div class="watermark" aria-hidden="true">Brightpath STEM Academy</div>

    <div class="footer-rule"></div>
    <div class="contact">
      <p class="contact__name">Dr. Velimir T. Osunde</p>
      <p class="contact__address">4417 Marbleton Lane, Fairfax Station, VA 22061</p>
      <p class="contact__phone">Phone: (703) 482–1630</p>
    </div>
  </div>
</body>
</html>
```